Company Introduction/Advertisement Flyer

We would like to redesign our current company line card. We send this printed flyer to prospective customers to introduce our company, the brands we represent and our competitive advantages. Our current design is very plain and simple, we'd like to have a little more design to the new version. Our website is www.valvequarryhub.com. We're a specialty supplier for plumbing material, specifically water and life safety products. Our customers are mostly male, blue-collar contractors, ages 40-60. I have included a pdf of our current flyer, and our high resolution transparent logo.

Requirements
Must have
• Phone number: (800) 314-2760
Website: www.valvequarryhub.com

```html
<!DOCTYPE html>
<html lang="en">
<head>
<meta charset="utf-8">
<title>Liberty Valve Supply Company — Line Card</title>
<link href="https://fonts.googleapis.com/css2?family=Montserrat:wght@300;400;500;600;700;800&display=swap" rel="stylesheet">
<style>
  :root {
    --brand-blue: #1a4aa8;
    --deep-blue: #1c4ea3;
    --brand-red: #b3121a;
    --dark-red: #8c0a10;
    --phone-red: #e2262b;
    --ink: #1d1d1f;
    --rule-grey: #a9a9a9;
    --divider: #ececec;
    --white: #ffffff;
    --badge: #d7dbe3;
  }
  * { box-sizing: border-box; margin: 0; padding: 0; }
  html, body { width: 745px; height: 1200px; overflow: hidden; background: var(--white); }
  body { font-family: "Montserrat", Arial, sans-serif; color: var(--ink); }
  .flyer { position: relative; width: 745px; height: 1200px; overflow: hidden; background: var(--white); }

  /* Header */
  .brand { position: absolute; left: 44px; top: 52px; display: flex; align-items: center; gap: 14px; }
  .brand-dot { width: 54px; height: 54px; border-radius: 50%; background: var(--brand-blue); }
  .brand-name { color: var(--brand-blue); font-weight: 400; line-height: 1; }
  .brand-name .primary { display: block; font-size: 35px; letter-spacing: -0.5px; }
  .brand-name .secondary { display: block; font-size: 18px; margin-top: 4px; }

  /* Hero */
  .hero-band { position: absolute; left: 0; top: 0; width: 745px; height: 620px; }
  .hero-copy { position: absolute; left: 45px; top: 230px; color: var(--white); }
  .hero-title { font-weight: 800; font-size: 42px; line-height: 46px; letter-spacing: 0.5px; }
  .hero-subtitle { margin-top: 12px; font-weight: 300; font-size: 30px; line-height: 33px; letter-spacing: 0.3px; }
  .hero-dash { width: 60px; height: 4px; background: var(--white); margin-top: 22px; }
  .hero-tagline { margin-top: 46px; font-weight: 600; font-size: 21px; letter-spacing: 0.3px; }
  .hero-photo { position: absolute; left: 460px; top: 30px; width: 285px; height: 556px; border-radius: 140px 140px 0 0;
    background: linear-gradient(180deg, #f2c21b 0%, #e9b98f 22%, #2a49b8 45%, #1b3596 100%); }

  /* Services */
  .services { position: absolute; left: 37px; top: 620px; width: 330px; }
  .services-title { color: var(--brand-blue); font-weight: 700; font-size: 27px; letter-spacing: 0.5px; }
  .services-rule { width: 58px; height: 3px; background: var(--rule-grey); margin-top: 10px; }
  .services-list { list-style: none; margin-top: 24px; }
  .services-list li { position: relative; padding-left: 37px; font-size: 15px; line-height: 18px; font-weight: 500; }
  .services-list li + li { margin-top: 20px; }
  .services-list li.single + li { margin-top: 22px; }
  .services-list svg { position: absolute; left: 0; top: 2px; }
  .column-divider { position: absolute; left: 372px; top: 612px; width: 1px; height: 420px; background: var(--divider); }

  /* Partner badges */
  .partners { position: absolute; left: 37px; top: 1064px; width: 326px; display: grid; gap: 12px 10px; }
  .partner-row { display: flex; justify-content: space-between; align-items: center; }
  .partner-badge { height: 18px; border-radius: 3px; background: var(--badge); }

  /* Products */
  .product { position: absolute; role: img; border-radius: 14px; }
  .product-kit { left: 440px; top: 614px; width: 270px; height: 190px;
    background: radial-gradient(circle at 35% 45%, #7c7f78 0%, #9a9d95 40%, rgba(255,255,255,0) 72%),
                radial-gradient(circle at 80% 40%, #e5e8e2 0%, rgba(255,255,255,0) 40%); }
  .product-valve { left: 420px; top: 830px; width: 290px; height: 165px;
    background: radial-gradient(ellipse at 50% 45%, #2c3240 0%, #5a5f6a 30%, #c9a36a 55%, rgba(255,255,255,0) 75%); }

  /* Contact */
  .call-label { position: absolute; left: 430px; top: 1010px; font-size: 19px; font-weight: 500; letter-spacing: 0.5px; }
  .call-phone { position: absolute; left: 428px; top: 1036px; font-size: 36px; font-weight: 700; color: var(--phone-red); letter-spacing: 0.5px; }
  .contact-panel { position: absolute; left: 0; top: 0; width: 745px; height: 1200px; pointer-events: none; }
  .contact-lines { position: absolute; left: 430px; top: 1116px; color: var(--white); font-size: 18px; font-weight: 500; line-height: 30px; letter-spacing: 0.6px; }
  .contact-lines .web { letter-spacing: 1.6px; }
</style>
</head>
<body>
<main class="flyer">

  <svg class="hero-band" viewBox="0 0 745 620" aria-hidden="true">
    <defs>
      <linearGradient id="heroRed" x1="0" y1="0" x2="1" y2="1">
        <stop offset="0" stop-color="#a5101a"/>
        <stop offset="0.6" stop-color="#b5151c"/>
        <stop offset="1" stop-color="#c8252b"/>
      </linearGradient>
    </defs>
    <polygon points="0,156 745,156 745,560 373,600 0,560" fill="url(#heroRed)"/>
    <polygon points="0,560 373,598 745,560 745,572 373,612 0,572" fill="var(--brand-blue)"/>
  </svg>

  <div class="brand">
    <span class="brand-dot"></span>
    <span class="brand-name">
      <span class="primary">Liberty Valve</span>
      <span class="secondary">Supply Company</span>
    </span>
  </div>

  <div class="hero-photo" role="img" aria-label="Photo of a smiling technician in a yellow hard hat and blue work coveralls, pointing at the headline"></div>

  <section class="hero-copy">
    <h1 class="hero-title">YOUR COMPLETE<br>SOURCE FOR</h1>
    <p class="hero-subtitle">Backflow Preventer<br>Repair Parts Accessories</p>
    <div class="hero-dash"></div>
    <p class="hero-tagline">Enclosures Test Gauge Calibration</p>
  </section>

  <section class="services">
    <h2 class="services-title">OUR SERVICES</h2>
    <div class="services-rule"></div>
    <ul class="services-list">
      <li><svg width="22" height="12" viewBox="0 0 22 12"><polygon points="11,0 22,12 0,12" fill="var(--brand-blue)"/><polygon points="11,5 16,10 6,10" fill="#fff"/></svg>Save gas and time by receiving parts at your doorstep</li>
      <li><svg width="22" height="12" viewBox="0 0 22 12"><polygon points="11,0 22,12 0,12" fill="var(--brand-blue)"/><polygon points="11,5 16,10 6,10" fill="#fff"/></svg>1-2 day delivery anywhere in the country</li>
      <li class="single"><svg width="22" height="12" viewBox="0 0 22 12"><polygon points="11,0 22,12 0,12" fill="var(--brand-blue)"/><polygon points="11,5 16,10 6,10" fill="#fff"/></svg>Same day shipping</li>
      <li class="single"><svg width="22" height="12" viewBox="0 0 22 12"><polygon points="11,0 22,12 0,12" fill="var(--brand-blue)"/><polygon points="11,5 16,10 6,10" fill="#fff"/></svg>No minimum orders</li>
      <li class="single"><svg width="22" height="12" viewBox="0 0 22 12"><polygon points="11,0 22,12 0,12" fill="var(--brand-blue)"/><polygon points="11,5 16,10 6,10" fill="#fff"/></svg>Online tracking of your order</li>
      <li class="single"><svg width="22" height="12" viewBox="0 0 22 12"><polygon points="11,0 22,12 0,12" fill="var(--brand-blue)"/><polygon points="11,5 16,10 6,10" fill="#fff"/></svg>Friendly, knowledgable staff</li>
      <li><svg width="22" height="12" viewBox="0 0 22 12"><polygon points="11,0 22,12 0,12" fill="var(--brand-blue)"/><polygon points="11,5 16,10 6,10" fill="#fff"/></svg>Technicians available to answer questions</li>
    </ul>
  </section>

  <div class="column-divider"></div>

  <div class="partners" aria-label="Partner brands">
    <div class="partner-row">
      <span class="partner-badge" style="width:54px"></span>
      <span class="partner-badge" style="width:42px"></span>
      <span class="partner-badge" style="width:62px"></span>
      <span class="partner-badge" style="width:60px"></span>
    </div>
    <div class="partner-row">
      <span class="partner-badge" style="width:70px"></span>
      <span class="partner-badge" style="width:72px"></span>
      <span class="partner-badge" style="width:62px"></span>
      <span class="partner-badge" style="width:50px"></span>
    </div>
    <div class="partner-row">
      <span class="partner-badge" style="width:24px"></span>
      <span class="partner-badge" style="width:50px"></span>
      <span class="partner-badge" style="width:48px"></span>
      <span class="partner-badge" style="width:62px"></span>
      <span class="partner-badge" style="width:62px"></span>
    </div>
  </div>

  <div class="product product-kit" role="img" aria-label="Photo of a grey backflow test kit case with a pressure gauge and coloured hoses"></div>
  <div class="product product-valve" role="img" aria-label="Photo of a backflow preventer valve assembly with brass fittings and blue handles"></div>

  <p class="call-label">CALL US NOW</p>
  <p class="call-phone">(800) 314-2760</p>

  <svg class="contact-panel" viewBox="0 0 745 1200" aria-hidden="true">
    <polygon points="440,1091 745,1091 745,1186 372,1186" fill="var(--deep-blue)"/>
    <polyline points="436,1091 368,1184 0,1184" fill="none" stroke="var(--brand-red)" stroke-width="2"/>
    <rect x="0" y="1188" width="745" height="12" fill="var(--deep-blue)"/>
  </svg>

  <div class="contact-lines">
    <p>24 hour Fax: (850) 314-2791</p>
    <p class="web">www.valvequarryhub.com</p>
  </div>

</main>
</body>
</html>
```